Bright Fern Custom Homes business card. Double sided. Modern. professional

Bright Fern Custom Homes
contemporary modern design with our logo /
Double sided with all our contact information
Use same Green colors as in our Logo. Contemporary logo that grabs your attention. Visually pleasing and balanced. Easy to read, and Vibrant. Would love an option for rounded edges. Embossed logo would be amazing.
Contact Information for Business Card
Dana Welk Owner / General Contractor Bright Fern Custom Homes p: 704.552.1830 m: 912.648.2071 e: brightferncustomhomes@mailbox.example w: www.brightferncustomhomes.example 218 Pryor Meadow Lane Fernwood, SC 29041

```html
<!DOCTYPE html>
<html lang="en">
<head>
<meta charset="utf-8">
<title>Bright Fern Custom Homes – Business Card</title>
<link rel="stylesheet" href="https://fonts.googleapis.com/css2?family=Cinzel:wght@400&family=Poppins:wght@400;600&display=swap">
<style>
  :root {
    --stage: #e8ebe3;
    --card-light: #f4f4f2;
    --card-dark: #050708;
    --green: #5f7b2d;
    --ink: #1c1c1c;
    --edge: #5a7328;
  }
  * { box-sizing: border-box; margin: 0; padding: 0; }
  html, body { width: 1200px; height: 958px; overflow: hidden; }
  body {
    background: var(--stage);
    display: flex;
    flex-direction: column;
    align-items: center;
    justify-content: center;
    gap: 60px;
  }
  .card {
    position: relative;
    width: 600px;
    height: 343px;
    border-radius: 14px;
    box-shadow: 0 4px 0 var(--edge), 0 18px 30px rgba(0,0,0,.18);
    overflow: hidden;
  }
  .card--back { background: var(--card-dark); }
  .card--front { background: var(--card-light); }

  .brand {
    position: absolute;
    display: flex;
    align-items: center;
    gap: 12px;
    font-family: "Cinzel", serif;
    font-weight: 400;
    color: var(--green);
    white-space: nowrap;
  }
  .brand__mark { background: var(--green); flex: none; }
  .card--back .brand {
    left: 50%; top: 50%;
    transform: translate(-50%, -50%);
    font-size: 44px;
    letter-spacing: 2px;
  }
  .card--back .brand__mark { width: 22px; height: 22px; }
  .card--front .brand {
    left: 300px; top: 64px;
    font-size: 26px;
    letter-spacing: 1px;
  }
  .card--front .brand__mark { width: 14px; height: 14px; }

  .contact {
    position: absolute;
    left: 40px; top: 130px;
    font-family: "Poppins", sans-serif;
    color: var(--ink);
  }
  .contact__company {
    font-weight: 600;
    color: var(--green);
    font-size: 15px;
  }
  .contact__address {
    font-weight: 600;
    font-size: 9.5px;
    padding-bottom: 5px;
    border-bottom: 1.5px solid var(--ink);
    width: 190px;
    white-space: nowrap;
    margin-bottom: 8px;
  }
  .contact__row {
    display: flex;
    align-items: center;
    gap: 9px;
    font-size: 13px;
    line-height: 21px;
  }
  .contact__row svg { width: 11px; height: 11px; fill: var(--green); flex: none; }
  .contact__web {
    font-weight: 600;
    color: var(--green);
    font-size: 13px;
    margin-top: 4px;
  }

  .person {
    position: absolute;
    right: 40px; bottom: 36px;
    text-align: right;
  }
  .person__name {
    font-family: "Cinzel", serif;
    font-size: 22px;
    color: var(--ink);
    letter-spacing: 1px;
  }
  .person__title {
    font-family: "Poppins", sans-serif;
    font-size: 12.5px;
    color: var(--green);
  }
</style>
</head>
<body>
  <section class="card card--back" aria-label="Card back">
    <div class="brand"><span class="brand__mark"></span>Bright Fern</div>
  </section>

  <section class="card card--front" aria-label="Card front">
    <div class="brand"><span class="brand__mark"></span>Bright Fern</div>

    <div class="contact">
      <p class="contact__company">Bright Fern Custom Homes</p>
      <p class="contact__address">218 Pryor Meadow Lane Fernwood, SC 29041</p>
      <p class="contact__row">
        <svg viewBox="0 0 12 12" aria-hidden="true"><path d="M1 4c0-2 2-3 5-3s5 1 5 3l-2 1-1-1.5H4L3 5 1 4zM2.5 6h7l1 5h-9z"/></svg>
        704.552.1830
      </p>
      <p class="contact__row">
        <svg viewBox="0 0 12 12" aria-hidden="true"><path d="M1 4c0-2 2-3 5-3s5 1 5 3l-2 1-1-1.5H4L3 5 1 4zM2.5 6h7l1 5h-9z"/></svg>
        912.648.2071
      </p>
      <p class="contact__row">
        <svg viewBox="0 0 12 12" aria-hidden="true"><path d="M0 2h12v8H0zM1 3l5 4 5-4v-.2H1z"/></svg>
        brightferncustomhomes@mailbox.example
      </p>
      <p class="contact__web">www.brightferncustomhomes.example</p>
    </div>

    <div class="person">
      <p class="person__name">Dana Welk</p>
      <p class="person__title">Owner / General Contractor</p>
    </div>
  </section>
</body>
</html>
```